Harbor Pine builders of ny Roofing flyer

We would like to create a flyer for roofing customers : commercial / real estate management / business / schools /warehouses

Flat roof specialists
Waterproofing experts

Special flat roof re layer @ 3.00 per sq ft

Roof leak repairs
Flashing
Waterproofing

Call 555 3019462

For pictures find torch down roof applications
Flat roofs ny

```html
<!DOCTYPE html>
<html lang="en">
<head>
<meta charset="utf-8">
<title>Harbor Pine builders of ny – Roofing Flyer</title>
<link href="https://fonts.googleapis.com/css2?family=Montserrat:wght@600;800;900&display=swap" rel="stylesheet">
<style>
  :root{
    --stage:#5b5b5b;
    --navy:#0b4a9a;
    --royal:#1463c4;
    --sky:#1a84e6;
    --ice:#e8f7ff;
    --paper-light:#f7f7f7;
    --paper-dark:#d4d4d4;
    --rule:#3a3a3a;
    --white:#ffffff;
  }
  html,body{margin:0;padding:0;width:1200px;height:1200px;overflow:hidden;background:var(--stage);}
  .flyer{position:absolute;left:226px;top:71px;width:748px;height:1058px;}
  .flyer svg{display:block;}
  text{font-family:'Montserrat',sans-serif;}
  .headline-outline{font-weight:900;fill:var(--ice);stroke:var(--royal);stroke-width:4px;paint-order:stroke;}
  .headline-solid{font-weight:900;fill:var(--navy);stroke:var(--white);stroke-width:4px;paint-order:stroke;}
  .service{font-weight:800;fill:var(--sky);}
  .sector{font-weight:800;fill:var(--navy);}
  .badge-text{font-weight:800;fill:var(--white);stroke:var(--navy);stroke-width:2px;paint-order:stroke;}
  .badge-price{font-weight:900;fill:var(--white);stroke:var(--navy);stroke-width:3px;paint-order:stroke;}
  .phone{font-weight:800;fill:var(--white);}
  .contact{font-weight:600;fill:var(--white);}
</style>
</head>
<body>
<div class="flyer">
<svg width="748" height="1058" viewBox="0 0 748 1058" xmlns="http://www.w3.org/2000/svg">
  <defs>
    <linearGradient id="paper" x1="0" y1="0" x2="1" y2="1">
      <stop offset="0" stop-color="var(--paper-dark)"/>
      <stop offset="0.45" stop-color="var(--paper-light)"/>
      <stop offset="1" stop-color="var(--paper-dark)"/>
    </linearGradient>
    <linearGradient id="photo-torch" x1="0" y1="0" x2="1" y2="1">
      <stop offset="0" stop-color="#e9e3dc"/><stop offset="0.5" stop-color="#c0704a"/><stop offset="1" stop-color="#8c8f96"/>
    </linearGradient>
    <linearGradient id="photo-flashing" x1="0" y1="0" x2="1" y2="1">
      <stop offset="0" stop-color="#b86a33"/><stop offset="1" stop-color="#5e5d60"/>
    </linearGradient>
    <linearGradient id="photo-membrane" x1="0" y1="0" x2="1" y2="1">
      <stop offset="0" stop-color="#7b7a76"/><stop offset="0.6" stop-color="#2b2f36"/><stop offset="1" stop-color="#4d7fc8"/>
    </linearGradient>
    <linearGradient id="photo-coating" x1="0" y1="0" x2="1" y2="1">
      <stop offset="0" stop-color="#a9b0ba"/><stop offset="0.55" stop-color="#8a8f98"/><stop offset="1" stop-color="#b68878"/>
    </linearGradient>
    <radialGradient id="badge-fill" cx="0.45" cy="0.35" r="0.7">
      <stop offset="0" stop-color="#2d8cf0"/><stop offset="1" stop-color="#0d4aa3"/>
    </radialGradient>
    <radialGradient id="icon-fill" cx="0.4" cy="0.35" r="0.7">
      <stop offset="0" stop-color="#3a95f0"/><stop offset="1" stop-color="#0c4a9e"/>
    </radialGradient>
  </defs>

  <!-- paper -->
  <rect class="paper" width="748" height="1058" fill="url(#paper)"/>

  <!-- photo areas -->
  <polygon role="img" aria-label="Photo: roofer in gloves drilling into a metal roof" points="457,0 748,0 748,413" fill="url(#photo-torch)"/>
  <polygon class="accent-stripe" points="348,0 370,0 455,93 433,93" fill="var(--royal)"/>
  <polygon role="img" aria-label="Photo: roofer hammering metal flashing onto shingles" points="114,356 373,356 491,484 196,484" fill="url(#photo-flashing)"/>
  <polygon role="img" aria-label="Photo: torch-down membrane roof application" points="401,356 748,356 748,483 513,483" fill="url(#photo-membrane)"/>
  <polygon role="img" aria-label="Photo: worker coating a tiled roof beside a paint bucket" points="0,264 296,590 0,919" fill="url(#photo-coating)"/>
  <polygon class="accent-stripe" points="0,960 176,768 196,768 0,984" fill="var(--royal)"/>

  <!-- headline -->
  <text class="headline-outline" x="81" y="93" font-size="58" textLength="298" lengthAdjust="spacingAndGlyphs">FLAT ROOF</text>
  <text class="headline-outline" x="81" y="142" font-size="58" textLength="332" lengthAdjust="spacingAndGlyphs">SPECIALISTS</text>
  <text class="headline-solid" x="83" y="208" font-size="78" textLength="276" lengthAdjust="spacingAndGlyphs">WATER</text>
  <text class="headline-solid" x="83" y="270" font-size="78" textLength="386" lengthAdjust="spacingAndGlyphs">PROOFING</text>
  <text class="headline-solid" x="82" y="332" font-size="78" textLength="322" lengthAdjust="spacingAndGlyphs">EXPERTS</text>

  <!-- services -->
  <polyline class="bracket" points="243,498 579,498 626,549" fill="none" stroke="var(--rule)" stroke-width="3"/>
  <polyline class="bracket" points="229,677 258,708 723,708" fill="none" stroke="var(--rule)" stroke-width="3"/>
  <text class="service" x="324" y="551" font-size="42" textLength="239" lengthAdjust="spacingAndGlyphs">ROOF LEAK</text>
  <text class="service" x="324" y="588" font-size="42" textLength="176" lengthAdjust="spacingAndGlyphs">REPAIRS</text>
  <line x1="326" y1="597" x2="722" y2="597" stroke="var(--rule)" stroke-width="2" stroke-dasharray="2 4"/>
  <text class="service" x="324" y="635" font-size="42" textLength="208" lengthAdjust="spacingAndGlyphs">FLASHING</text>
  <line x1="326" y1="646" x2="722" y2="646" stroke="var(--rule)" stroke-width="2" stroke-dasharray="2 4"/>
  <text class="service" x="326" y="686" font-size="42" textLength="374" lengthAdjust="spacingAndGlyphs">WATERPROOFING</text>

  <!-- sectors -->
  <g class="sector-icons" fill="url(#icon-fill)" stroke="#dfe9f7" stroke-width="1.5" stroke-dasharray="1.5 2">
    <circle cx="351" cy="738" r="17"/>
    <circle cx="351" cy="792" r="17"/>
    <circle cx="351" cy="845" r="17"/>
    <circle cx="351" cy="894" r="17"/>
    <circle cx="351" cy="946" r="17"/>
  </g>
  <g class="sector-glyphs" fill="none" stroke="var(--white)" stroke-width="1.6">
    <rect x="344" y="730" width="9" height="16"/><rect x="353" y="735" width="6" height="11"/>
    <path d="M342 800 v-9 l6 -5 l6 5 v9 M354 800 v-12 h6 v12"/>
    <path d="M341 846 l5 -4 l5 3 l5 -3 l5 4 l-5 5 l-5 -3 l-5 3 z"/>
    <path d="M341 902 h20 M343 902 v-8 h16 v8 M342 894 l9 -6 l9 6"/>
    <path d="M342 953 v-12 h10 v12 M352 953 v-7 h8 v7"/>
  </g>
  <text class="sector" x="381" y="749" font-size="29" textLength="183" lengthAdjust="spacingAndGlyphs">COMMERCIAL</text>
  <text class="sector" x="381" y="790" font-size="29" textLength="185" lengthAdjust="spacingAndGlyphs">REAL ESTATE</text>
  <text class="sector" x="381" y="815" font-size="29" textLength="198" lengthAdjust="spacingAndGlyphs">MANAGEMENT</text>
  <text class="sector" x="381" y="856" font-size="29" textLength="132" lengthAdjust="spacingAndGlyphs">BUSINESS</text>
  <text class="sector" x="381" y="905" font-size="29" textLength="129" lengthAdjust="spacingAndGlyphs">SCHOOLS</text>
  <text class="sector" x="381" y="957" font-size="29" textLength="195" lengthAdjust="spacingAndGlyphs">WAREHOUSES</text>

  <!-- offer badge -->
  <g class="offer-badge">
    <circle cx="230" cy="873" r="88" fill="url(#badge-fill)"/>
    <circle cx="230" cy="873" r="80" fill="none" stroke="#8cc3ff" stroke-width="2" stroke-dasharray="8 5"/>
    <text class="badge-text" x="230" y="826" font-size="17" text-anchor="middle">SPECIAL</text>
    <text class="badge-text" x="230" y="842" font-size="17" text-anchor="middle">FLAT ROOF</text>
    <text class="badge-text" x="230" y="858" font-size="17" text-anchor="middle">RE LAYER</text>
    <text class="badge-price" x="230" y="896" font-size="44" text-anchor="middle" textLength="146" lengthAdjust="spacingAndGlyphs">@3.00</text>
    <text class="badge-text" x="230" y="921" font-size="20" text-anchor="middle">PER SQ FT</text>
  </g>

  <!-- contact band -->
  <polygon class="contact-band" points="0,984 558,984 615,1046 0,1046" fill="var(--royal)"/>
  <g class="phone-icon" fill="none" stroke="#9fd0ff" stroke-width="3" stroke-linecap="round">
    <path d="M28 1002 c-6 6 -4 16 4 24 c8 8 18 10 24 4 l-5 -6 c-3 2 -7 2 -12 -3 c-5 -5 -5 -9 -3 -12 z"/>
    <path d="M40 1001 a10 10 0 0 1 9 9 M41 995 a16 16 0 0 1 14 14"/>
  </g>
  <text class="phone" x="60" y="1032" font-size="46" textLength="278" lengthAdjust="spacingAndGlyphs">555 3019462</text>
  <text class="contact" x="359" y="1009" font-size="16" textLength="196" lengthAdjust="spacingAndGlyphs">hello@harborpinebuilders.com</text>
  <text class="contact" x="359" y="1030" font-size="16" textLength="196" lengthAdjust="spacingAndGlyphs">www.harborpinebuilders.com</text>
</svg>
</div>
</body>
</html>
```